Business Card Design for Small Electrical Contractor

I need to update my business card into something a little more modern. We are a small electrical contracting company. We service domestic and commercial places around Sydney. We have 2 logo designs at the moment. I have uploaded both and 2 different sizes to work with.

Industry/Entity Type

Business

Contact Information for Business Card

Leo Hartigan
8/21-23 Birch Rd, Kelsworth 2087
t - (02) 9381 4720
m - 0427 815 903
E - info@hartiganelx.com.au
W - hartiganelx.com.au
ABN: 42 907 551 316

Font styles to use
Sans Serif

Requirements
Must have
• I would also like to see the below fit on somewhere aswell
• - Licensed Electrician
• - Level 2 (Cat 1 & 4)
• - Domestic
• - Commercial
• - Repairs and Installations
• - Data
Nice to have
• Try and keep similar colours as logo
Should not have
• No lightning bolts or light globes. Smart and professional please.

```html
<!DOCTYPE html>
<html lang="en">
<head>
<meta charset="utf-8">
<title>Hartigan Electrical Co. – Business Cards</title>
<link rel="stylesheet" href="https://fonts.googleapis.com/css2?family=Montserrat:wght@500;600;700&family=Roboto:wght@400;500&display=swap">
<style>
  :root {
    --backdrop: #2b2b2b;
    --card-white: #fbfbfb;
    --brand-green: #0f3b36;
    --brand-orange: #e08a1e;
    --text-light: #e9eeec;
    --text-muted: #b9c7c3;
  }
  * { box-sizing: border-box; margin: 0; padding: 0; }
  html, body { width: 1200px; height: 997px; overflow: hidden; }
  body {
    background: var(--backdrop);
    display: flex; flex-direction: column; align-items: center; justify-content: center;
    gap: 60px;
    font-family: "Roboto", Arial, sans-serif;
  }
  .card {
    position: relative;
    width: 620px; height: 379px;
    border-radius: 22px;
    background: var(--card-white);
    overflow: hidden;
  }
  .brand-name {
    display: flex; align-items: center; gap: 12px;
    font-family: "Montserrat", Arial, sans-serif;
    font-weight: 700;
    color: var(--brand-green);
    letter-spacing: 0.5px;
  }
  .brand-dot {
    border-radius: 50%;
    background: var(--brand-orange);
    flex: none;
  }

  /* Contact side */
  .contact-card .brand-name {
    position: absolute; top: 58px; right: 44px; font-size: 24px;
  }
  .contact-card .brand-dot { width: 14px; height: 14px; }
  .contact-band {
    position: absolute; left: 0; right: 0; bottom: 0; height: 206px;
    background: var(--brand-green);
    border-top: 6px solid var(--brand-orange);
  }
  .notch {
    position: absolute; width: 0; height: 0;
    border-left: 10px solid transparent; border-right: 10px solid transparent;
    border-top: 11px solid var(--brand-orange);
  }
  .contact-band .notch { top: -1px; left: 44px; }
  .person { position: absolute; left: 44px; top: 26px; }
  .person-name { font-size: 24px; font-weight: 500; color: var(--text-light); }
  .person-role { font-size: 15px; color: var(--brand-orange); margin-top: 2px; }
  .contact-list { position: absolute; left: 44px; top: 92px; list-style: none; }
  .contact-list li {
    display: flex; align-items: center; gap: 12px;
    font-size: 15px; color: var(--text-light); height: 24px;
  }
  .contact-icon {
    width: 17px; height: 17px; border-radius: 50%;
    background: var(--brand-orange);
    display: flex; align-items: center; justify-content: center;
  }
  .contact-list .web { color: var(--brand-orange); font-weight: 500; }
  .company-details {
    position: absolute; right: 44px; top: 26px; text-align: right;
    font-size: 12px; color: var(--text-muted); line-height: 1.6;
  }
  .company-address { position: absolute; right: 44px; bottom: 34px; text-align: right; }
  .company-address .legal-name { font-size: 15px; font-weight: 500; color: var(--brand-orange); }
  .company-address .street { font-size: 14px; color: var(--text-light); margin-top: 3px; }

  /* Brand side */
  .brand-card .brand-name {
    position: absolute; top: 112px; left: 0; right: 0; justify-content: center;
    font-size: 38px;
  }
  .brand-card .brand-dot { width: 22px; height: 22px; }
  .services-band {
    position: absolute; left: 0; right: 0; bottom: 0; height: 96px;
    background: var(--brand-green);
    border-top: 6px solid var(--brand-orange);
    display: flex; align-items: center; justify-content: center;
  }
  .services-band .notch { top: -1px; left: 300px; }
  .services-list { display: flex; gap: 20px; list-style: none; }
  .services-list li {
    font-family: "Montserrat", Arial, sans-serif; font-weight: 600;
    font-size: 17px; color: var(--text-light);
    display: flex; align-items: center; gap: 8px;
  }
  .services-list li::before {
    content: ""; width: 6px; height: 6px; border-radius: 50%; background: var(--brand-orange);
  }
</style>
</head>
<body>

<section class="card contact-card">
  <div class="brand-name"><span class="brand-dot"></span>Hartigan Electrical Co.</div>
  <div class="contact-band">
    <span class="notch"></span>
    <div class="person">
      <p class="person-name">Leo Hartigan</p>
      <p class="person-role">Licensed Electrician</p>
    </div>
    <ul class="contact-list">
      <li><span class="contact-icon"><svg width="10" height="10" viewBox="0 0 10 10"><path d="M2 1h2l1 2.3-1.2.8a5 5 0 0 0 2.1 2.1l.8-1.2L9 6v2a1 1 0 0 1-1 1A7 7 0 0 1 1 2a1 1 0 0 1 1-1z" fill="#0f3b36"/></svg></span>(02) 9381 4720</li>
      <li><span class="contact-icon"><svg width="10" height="10" viewBox="0 0 10 10"><rect x="2.5" y="0.5" width="5" height="9" rx="1" fill="#0f3b36"/><rect x="3.5" y="1.8" width="3" height="5" fill="#e08a1e"/></svg></span>0427 815 903</li>
      <li><span class="contact-icon"><svg width="10" height="10" viewBox="0 0 10 10"><rect x="0.5" y="2" width="9" height="6" fill="#0f3b36"/><path d="M0.8 2.3 5 5.5l4.2-3.2" stroke="#e08a1e" stroke-width="0.9" fill="none"/></svg></span>info@hartiganelx.com.au</li>
      <li class="web">www.hartiganelx.com.au</li>
    </ul>
    <div class="company-details">
      <p>ABN: 42 907 551 316</p>
      <p>Level 2 (Cat 1 &amp; 4)</p>
    </div>
    <div class="company-address">
      <p class="legal-name">Hartigan Electrical Co. Pty</p>
      <p class="street">8/21-23 Birch Rd, Kelsworth 2087</p>
    </div>
  </div>
</section>

<section class="card brand-card">
  <div class="brand-name"><span class="brand-dot"></span>Hartigan Electrical Co.</div>
  <div class="services-band">
    <span class="notch"></span>
    <ul class="services-list">
      <li>Domestic</li>
      <li>Commercial</li>
      <li>Repairs &amp; Installations</li>
      <li>Data</li>
    </ul>
  </div>
</section>

</body>
</html>
```